Business Card Design needed for logo design project

Our company needs a Business Card Design. Please refer to our original project in the link above.

Industry/Entity Type

Business

```html
<!DOCTYPE html>
<html lang="en">
<head>
<meta charset="utf-8">
<title>Vantrel Business Card</title>
<link href="https://fonts.googleapis.com/css2?family=Cabin:wght@400;500&display=swap" rel="stylesheet">
<style>
  :root {
    --backdrop: #e6e5e3;
    --card: #fbfbf9;
    --ink: #1e1e1e;
    --ink-soft: #2c2c2c;
    --rule: #8f8f8f;
    --rule-light: #d6d3cf;
    --icon: #9a9a9a;
    --edge: #a9a9a9;
  }
  * { margin: 0; padding: 0; box-sizing: border-box; }
  html, body {
    width: 1200px; height: 576px; overflow: hidden;
    background: var(--backdrop);
    font-family: "Cabin", "Gill Sans", sans-serif;
    color: var(--ink);
  }
  .business-card {
    position: absolute; left: 220px; top: 72px;
    width: 760px; height: 432px;
    background: var(--card);
    border-left: 10px solid var(--edge);
    box-shadow: 0 4px 14px rgba(0,0,0,0.18);
  }
  .card-lines { position: absolute; inset: 0; }
  .brand-name {
    position: absolute; left: 48px; top: 28px;
    font-size: 92px; font-weight: 400; letter-spacing: 3px;
    line-height: 1; color: var(--ink);
  }
  .icon { position: absolute; width: 22px; height: 22px; }
  .contact-text {
    position: absolute; font-size: 20px; font-weight: 500;
    color: var(--ink-soft); line-height: 1.25; letter-spacing: 0.5px;
  }
  .person-name { left: 96px; top: 160px; }
  .phone { left: 96px; top: 188px; }
  .phone-icon { left: 56px; top: 188px; }
  .email { left: 96px; top: 256px; }
  .email-icon { left: 52px; top: 258px; }
  .address { left: 508px; top: 316px; }
  .pin-icon { left: 470px; top: 318px; }
  .website { left: 508px; top: 384px; }
  .globe-icon { left: 470px; top: 384px; }
</style>
</head>
<body>
  <section class="business-card">
    <svg class="card-lines" width="750" height="432" viewBox="0 0 750 432" aria-hidden="true">
      <line x1="48" y1="150" x2="360" y2="150" stroke="var(--rule-light)" stroke-width="1.5"/>
      <path d="M0 238 H370 L392 222 H470" fill="none" stroke="var(--rule)" stroke-width="1.5"/>
      <path d="M392 238 L440 300 H750" fill="none" stroke="var(--rule)" stroke-width="1.5"/>
    </svg>

    <div class="brand-name">vantrel</div>

    <div class="contact-text person-name">YOUR NAME</div>
    <svg class="icon phone-icon" viewBox="0 0 24 24" aria-hidden="true">
      <path d="M6.6 3.5c.6-.4 1.4-.2 1.7.4l1.6 3c.3.6.1 1.2-.4 1.6l-1.2.9c.9 2.1 2.5 3.9 4.5 5l1-1.1c.4-.5 1.1-.6 1.6-.3l2.9 1.8c.6.4.8 1.2.3 1.8l-1.4 1.8c-.6.8-1.7 1.1-2.7.7C9.5 17.4 6.4 14 5 9.6c-.3-1 0-2 .8-2.6z" fill="var(--icon)"/>
    </svg>
    <div class="contact-text phone">555-210-4830</div>

    <svg class="icon email-icon" viewBox="0 0 24 24" aria-hidden="true">
      <rect x="2.5" y="5.5" width="19" height="13" fill="none" stroke="var(--icon)" stroke-width="1.6"/>
      <path d="M2.5 5.5 L12 13 L21.5 5.5" fill="none" stroke="var(--icon)" stroke-width="1.6"/>
    </svg>
    <div class="contact-text email">info@vantrel.com</div>

    <svg class="icon pin-icon" viewBox="0 0 24 24" aria-hidden="true">
      <path d="M12 2a7 7 0 0 0-7 7c0 5 7 13 7 13s7-8 7-13a7 7 0 0 0-7-7z" fill="var(--icon)"/>
      <circle cx="12" cy="9" r="2.6" fill="var(--card)"/>
    </svg>
    <div class="contact-text address">48 Marlow Lane<br>Harbor City CA-90210</div>

    <svg class="icon globe-icon" viewBox="0 0 24 24" aria-hidden="true">
      <circle cx="12" cy="12" r="9.5" fill="none" stroke="var(--icon)" stroke-width="1.6"/>
      <ellipse cx="12" cy="12" rx="4" ry="9.5" fill="none" stroke="var(--icon)" stroke-width="1.4"/>
      <line x1="2.5" y1="12" x2="21.5" y2="12" stroke="var(--icon)" stroke-width="1.4"/>
      <line x1="4" y1="7" x2="20" y2="7" stroke="var(--icon)" stroke-width="1.2"/>
      <line x1="4" y1="17" x2="20" y2="17" stroke="var(--icon)" stroke-width="1.2"/>
    </svg>
    <div class="contact-text website">www.vantrel.com</div>
  </section>
</body>
</html>
```